International Marketing Company - Web Design Project

vLumo is a well-funded start up in London developing an Online Marketing Platform for small businesses in Europe.

We require a large number of high quality business web designs for our business website builder. Our business websites are completely integrated into our Online Marketing systems and therefore it is important for designers to comply with our Design Guidelines.

This initial contest is a trial for us to open up the design process to top designers for the Builders vertical (e.g. Builders, Electricians, Plumbers, Flooring, etc.). We have implemented a base html structure and design and included them in the files.

Use your creativity to design new and fresh designs based on the included elements (e.g. testimonials, business description, etc).

We will award the stated prize money for the top three designs.

Any designers that submit designs we feel are of a high enough quality but do not make the top 3 could still be compensated and WILL be invited to participate in our next vertical competition.

Therefore, we encourage designers to submit as many designs as possible as we may award up to 25 designs.

Submissions will be reviewed daily and feedback provided where possible.

Designers who can also code will have the options to implement their designs for an additional fee.

Good luck!
Updates

There has been a mistake made in regard to the prize. Pixel Harbor should have it fixed soon.

1st place = £350
2nd place = £250
3rd Place = £150

Thanks,
Rowan
25/11/2011

UPDATE:

1st place will win £350
2nd place will win £250
3rd place will win £150

Everything else is as to the specification.

Thanks
Rowan

Target Market(s)

Builders, Electricians, Plumbers, Tradesman, Small construction companies

Industry/Entity Type

Business

Requirements
Must have
• Totally new designs based around the elements we want to show on each page.

We are looking for something different to the design we already have. But you can use that as a starting point.

Use the included files to see what is required for each page. Here is a brief outline:

Homepage - Testimonials, News, Business Description, Latest Projects and Call to action

About-Us - Team Summary, About the Business and a call to action

Projects Page - Project Details (Oage Title and description), Each project needs a title, content and 2 images.

Testimonials Page - The testifiers name and their comment

Contacts Page - Trelwyn Map, Company address, business hours, contact form and a call to action.

Please submit final designs in Photoshop or Fireworks format.

Each page has a set of elements. These element must feature in the design of that page. See supporting documents for page details.

All elements must be included in your design. Please do not add any extra element.

Professional look and feel
Nice to have
• Design variations:
Full width designs
Boxed Designs
With AND without carousels
OR static images
Good use of stock images.

Creative use of the elements, dont be restricted/influenced by the default design we have already

Designs based on the 960 grid

```html
<!DOCTYPE html>
<html lang="en">
<head>
<meta charset="utf-8">
<title>Kestrel Electrical – Home</title>
<link rel="stylesheet" href="https://fonts.googleapis.com/css2?family=Arimo:wght@400;700&family=Noto+Sans:wght@400;700&display=swap">
<style>
:root{
  --page:#f2f2f2;
  --frame-top:#6a8cc0;
  --frame-bottom:#3f63a3;
  --brand-deep:#1a3a9a;
  --nav:#221a60;
  --call:#1a8ad0;
  --call-light:#2ea0e0;
  --side:#ececec;
  --heading:#1555a8;
  --link:#1a55a8;
  --body-grey:#8a8a8a;
  --bar-grey:#b3b3b3;
  --projects:#16378c;
  --footer:#1e3a8a;
  --white:#ffffff;
  --black:#000000;
}
*{box-sizing:border-box;margin:0;padding:0}
html,body{width:1200px;height:900px;overflow:hidden;background:var(--page)}
body{position:relative;font-family:"Noto Sans",Verdana,sans-serif}
.site-frame{position:absolute;left:72px;top:46px;width:1023px;height:768px;
  background:linear-gradient(180deg,var(--frame-top),var(--frame-bottom));
  box-shadow:3px 4px 6px rgba(0,0,0,.35)}
.header{position:absolute;left:107px;top:46px;width:953px;height:195px;background:var(--brand-deep)}
.header-visual{position:absolute;left:288px;top:0;width:665px;height:195px;
  background:radial-gradient(ellipse at 35% 50%,#3a66c8 0%,#1e46a8 45%,#12308a 100%)}
.brand{position:absolute;left:40px;top:70px;z-index:2;font-family:"Arimo",sans-serif;font-weight:700;font-size:40px;color:var(--white);white-space:nowrap}
.call-banner{position:absolute;left:647px;top:0;width:306px;height:94px;z-index:2;
  background:linear-gradient(180deg,var(--call-light),var(--call));
  box-shadow:2px 3px 5px rgba(0,0,0,.4);color:var(--white);font-family:"Arimo",sans-serif;white-space:nowrap}
.call-banner .label{position:absolute;left:14px;top:12px;font-size:25px;font-weight:700}
.call-banner .number{position:absolute;left:94px;top:12px;font-size:27px;font-weight:700}
.call-banner .sub{position:absolute;left:94px;top:52px;font-size:19px}
.nav{position:absolute;left:107px;top:242px;width:953px;height:43px;background:var(--nav);border-top:1px solid #4a5aa0}
.nav a{position:absolute;top:15px;font-family:"Arimo",sans-serif;font-size:13px;color:var(--white);text-decoration:none;white-space:nowrap}
.nav .active{text-shadow:0 0 10px rgba(255,255,255,.8)}
.sidebar{position:absolute;left:107px;top:285px;width:285px;height:492px;background:var(--side)}
.sidebar h2{font-family:"Arimo",sans-serif;font-size:19px;color:var(--heading);position:absolute;white-space:nowrap}
.sidebar p{position:absolute;font-size:11px;line-height:20px;color:var(--link);white-space:nowrap}
.more-arrow{font-family:"Arimo",sans-serif;font-weight:700;font-size:19px;line-height:10px}
.welcome{position:absolute;left:392px;top:285px;width:666px;height:263px;background:var(--white)}
.welcome h1{position:absolute;left:18px;top:23px;font-family:"Arimo",sans-serif;font-size:19px;color:var(--heading);white-space:nowrap}
.welcome p{position:absolute;left:21px;font-size:12.6px;font-weight:700;line-height:20px;letter-spacing:.5px;color:var(--body-grey);white-space:nowrap}
.projects-bar{position:absolute;left:392px;top:550px;width:470px;height:45px;background:var(--bar-grey)}
.projects-bar h2{position:absolute;left:25px;top:11px;font-family:"Arimo",sans-serif;font-size:19px;color:var(--white)}
.projects{position:absolute;left:392px;top:595px;width:470px;height:182px;background:var(--projects)}
.project-photo{position:absolute;left:12px;top:24px;width:239px;height:135px;border:3px solid #9a9a9a;
  background:linear-gradient(135deg,#6b5a3a 0%,#c8a448 40%,#8a8a84 70%,#d8d8d4 100%)}
.projects p{position:absolute;left:266px;top:34px;font-size:10.5px;line-height:20px;color:var(--white);white-space:nowrap}
.quote-box{position:absolute;left:862px;top:551px;width:196px;height:221px;background:var(--white);border:1px solid #9a9a9a;box-shadow:1px 2px 3px rgba(0,0,0,.3)}
.quote-box .head{height:37px;background:var(--call);color:var(--white);font-family:"Arimo",sans-serif;font-weight:700;font-size:14px;padding:11px 0 0 11px;white-space:nowrap}
.quote-box .head span{color:var(--black)}
.quote-box p{position:absolute;left:17px;top:50px;font-size:12.6px;font-weight:700;line-height:20px;letter-spacing:.3px;color:var(--body-grey);white-space:nowrap}
.quote-box hr{position:absolute;left:22px;top:146px;width:160px;border:0;border-top:2px solid #a8a8a8}
.quote-box .phone{position:absolute;left:7px;top:172px;font-family:"Arimo",sans-serif;font-weight:700;font-size:13px;color:var(--body-grey);white-space:nowrap}
.quote-box .phone b{color:var(--call);font-size:16px;margin-left:5px}
.footer{position:absolute;left:105px;top:777px;width:957px;height:36px;background:var(--footer);color:var(--white);font-size:10.5px;padding:13px 0 0 364px;white-space:nowrap}
</style>
</head>
<body>
<div class="site-frame"></div>

<header class="header">
  <div class="header-visual" role="img" aria-label="Blue electric lightning and swirl artwork"></div>
  <div class="brand">KESTREL</div>
  <div class="call-banner">
    <span class="label">CALL</span>
    <span class="number">020 7946 0321</span>
    <span class="sub">For Free Quote</span>
  </div>
</header>

<nav class="nav">
  <a class="active" style="left:327px">HOME</a>
  <a style="left:452px">ABOUT US</a>
  <a style="left:591px">TESTIMONIALS</a>
  <a style="left:740px">PORTFOLIO</a>
  <a style="left:857px;top:16px">CONTACTS</a>
</nav>

<aside class="sidebar">
  <h2 style="left:20px;top:23px">Customers say</h2>
  <p style="left:20px;top:57px">Kestrel Electrical are the best electriciians in Crawley.<br>They are experts in all areas of house electrical<br>and I am extremely satisfied with my new loft<br>conversion.more &gt;&gt;<br>Mr. Halvorsen<br><br>I rarely write references for anyone, but Kestrel<br>Electrical in Crawley are outstanding. They<br>restored my Crawley home to a very high specifi-<br>cation and the team are very approachable and<br>friendly.more &gt;&gt;<br>Mr. Penrith</p>
  <h2 style="left:22px;top:325px">Latest News</h2>
  <p style="left:23px;top:360px">Kestrel Electrical have just finished<br>another fine job in Crawley. more &gt;&gt;<br>Timber frames seem to be all the rage<br>in London. Using the latest in wood<br>tech! more <span class="more-arrow">&gt;&gt;</span></p>
</aside>

<main>
  <section class="welcome">
    <h1>Welcome to Kestrel Electrical</h1>
    <p style="top:60px">I am an experienced electrican in Crawley, Kestrel Electrical have been based in Crawley<br>for over 10 years. My team and I are proven, reliable electricians in Crawley. We've<br>come across a lot in our time, so don't hesitate to get in touch about any electrical<br>project.</p>
    <p style="top:160px">I am a friendly, electrician who has built a team of excellent tradesmen based in Craw-<br>ley. My electricians in Crawley have years of experience in kitchen renovation, bath-<br>room renovation, roofing and electrical plumbing, loft conversions and house restora-<br>tion.</p>
  </section>

  <div class="projects-bar"><h2>Latest Projects</h2></div>
  <section class="projects">
    <div class="project-photo" role="img" aria-label="Electrician in a yellow hard hat working on wiring"></div>
    <p>Kestrel Electrical have just finished<br>another fine job in Crawley. more &gt;&gt;<br>Timber frames seem to be all the rage<br>in London. Using the latest in wood<br>tech! more <span class="more-arrow">&gt;&gt;</span></p>
  </section>

  <aside class="quote-box">
    <div class="head">CALL FOR <span>FREE QUOTE</span></div>
    <p>Call now to discuss how<br>we can help. My quotes<br>are always free with no<br>obligation</p>
    <hr>
    <div class="phone">Phone: <b>020 7946 0321</b></div>
  </aside>
</main>

<footer class="footer">KESTREL ELECTRICAL 48 Ferncliff Road, Crawley, RH10 3QT &nbsp;Phone 020 7946 0321 Fax 020 7946 0322</footer>
</body>
</html>
```